Halvorsen Partners Business Card

Halvorsen Partners Civil Construction
Marcus Halvorsen
CEO
727-518-6094
Marcus@HalvorsenSiteworks.example
www.HalvorsenSiteworks.example
Site Development
Utility Construction
Excavation
40876 County Lane 19
Pell Harbor, FL 34000

Target Market(s)

Construction and government

Industry/Entity Type

Business

Contact Information for Business Card

I want an unique design that make a statement

Number of Pages Required

1 page

Font styles to use

Colors

Designer to choose colors to be used in the design.

Requirements
Must have
• unique design, feel free to modify or change the color of my logo.
Nice to have
• extra design features like spot UV, foil accents, color edges, unique paper, or any thing that would make my card pop.
• I like the feel of the image that I attached

```html
<!DOCTYPE html>
<html lang="en">
<head>
<meta charset="utf-8">
<title>Halvorsen Partners Business Card</title>
<link href="https://fonts.googleapis.com/css2?family=Lato:wght@300;400;700;900&display=swap" rel="stylesheet">
<style>
  :root {
    --brand-purple: #352c6e;
    --band-purple: #4a4384;
    --ink: #333333;
    --paper: #ffffff;
    --rule: #b9b9c4;
  }
  * { margin: 0; padding: 0; box-sizing: border-box; }
  html, body { width: 1200px; height: 1000px; overflow: hidden; background: var(--paper); }
  body { position: relative; font-family: "Lato", "Helvetica Neue", Arial, sans-serif; }
  .card-art { position: absolute; left: 0; top: 0; width: 1200px; height: 1000px; }

  .brand-lockup {
    position: absolute; left: 250px; top: 82px;
    display: flex; align-items: center; gap: 22px;
  }
  .brand-lockup .brand-square { width: 78px; height: 78px; background: var(--brand-purple); }
  .brand-name {
    color: var(--brand-purple); font-weight: 900; font-size: 42px;
    letter-spacing: 0.5px; text-transform: uppercase; white-space: nowrap;
  }

  .holder-line {
    position: absolute; left: 250px; top: 212px;
    font-size: 33px; color: var(--ink); font-weight: 900; letter-spacing: 0.5px;
    white-space: nowrap;
  }
  .holder-line .divider { color: var(--brand-purple); font-weight: 400; margin: 0 6px; }
  .holder-line .title { color: var(--brand-purple); font-weight: 400; }

  .contact-block {
    position: absolute; right: 255px; top: 296px; text-align: right;
  }
  .contact-phone { font-size: 34px; font-weight: 900; color: var(--ink); letter-spacing: 0.5px; }
  .contact-email { font-size: 25px; font-weight: 400; color: var(--brand-purple); margin-top: 4px; }
  .contact-web { font-size: 33px; font-weight: 900; color: var(--ink); margin-top: 18px; }

  .back-lockup {
    position: absolute; left: 0; width: 1200px; top: 640px;
    display: flex; justify-content: center; align-items: center; gap: 18px;
  }
  .back-lockup .brand-square { width: 56px; height: 56px; background: var(--brand-purple); }
  .back-lockup .brand-name { font-size: 36px; }

  .services {
    position: absolute; right: 545px; top: 843px; text-align: right;
    color: var(--paper); font-weight: 900; font-size: 23px; line-height: 31px;
    white-space: nowrap;
  }
  .address {
    position: absolute; left: 685px; top: 845px;
    color: var(--paper); font-weight: 400; font-size: 23px; line-height: 29px;
    letter-spacing: 0.5px; white-space: nowrap;
  }
</style>
</head>
<body>
<svg class="card-art" width="1200" height="1000" viewBox="0 0 1200 1000">
  <defs>
    <linearGradient id="skyFade" x1="0" y1="0" x2="0" y2="1">
      <stop offset="0" stop-color="#ffffff" stop-opacity="0"/>
      <stop offset="0.55" stop-color="#e8f0f7"/>
      <stop offset="1" stop-color="#cfe0ec"/>
    </linearGradient>
    <linearGradient id="edgeShade" x1="0" y1="0" x2="1" y2="0">
      <stop offset="0" stop-color="#d9d9e2"/>
      <stop offset="1" stop-color="#ffffff" stop-opacity="0"/>
    </linearGradient>
  </defs>

  <g class="card-front">
    <rect x="200" y="10" width="797" height="478" fill="var(--paper)"/>
    <rect x="200" y="260" width="797" height="228" fill="url(#skyFade)" role="img" aria-label="Faint city skyline backdrop"/>
    <path d="M200 10 L230 10 C205 120 200 220 220 300 L200 325 Z" fill="url(#edgeShade)"/>
    <path d="M800 10 C900 60 980 140 997 230 L997 10 Z" fill="#ececf2"/>
    <polygon points="833,10 997,10 997,175" fill="var(--brand-purple)"/>
    <polygon points="200,325 200,488 365,488" fill="var(--brand-purple)"/>
    <polyline points="218,48 218,31 830,31" fill="none" stroke="var(--brand-purple)" stroke-width="4"/>
    <polyline points="370,470 979,470 979,452" fill="none" stroke="var(--brand-purple)" stroke-width="4"/>
    <line x1="250" y1="197" x2="840" y2="197" stroke="var(--rule)" stroke-width="1.5"/>
  </g>

  <g class="card-back">
    <rect x="200" y="512" width="797" height="476" fill="var(--paper)"/>
    <rect x="200" y="640" width="797" height="180" fill="url(#skyFade)" role="img" aria-label="Faint city skyline backdrop"/>
    <rect x="200" y="925" width="797" height="63" fill="#eef3f8" role="img" aria-label="Reflected skyline fade"/>
    <rect x="200" y="820" width="797" height="105" fill="var(--band-purple)"/>
    <line x1="669" y1="833" x2="669" y2="912" stroke="var(--paper)" stroke-width="1.5"/>
    <polyline points="218,548 218,531 979,531 979,548" fill="none" stroke="var(--brand-purple)" stroke-width="4"/>
    <polyline points="218,950 218,968 979,968 979,950" fill="none" stroke="var(--brand-purple)" stroke-width="4"/>
  </g>
</svg>

<div class="brand-lockup">
  <span class="brand-square"></span>
  <span class="brand-name">Halvorsen Partners</span>
</div>

<div class="holder-line">MARCUS HALVORSEN<span class="divider">|</span><span class="title">CEO</span></div>

<div class="contact-block">
  <div class="contact-phone">727-518-6094</div>
  <div class="contact-email">Marcus@HalvorsenSiteworks.example</div>
  <div class="contact-web">www.HalvorsenSiteworks.example</div>
</div>

<div class="back-lockup">
  <span class="brand-square"></span>
  <span class="brand-name">Halvorsen Partners</span>
</div>

<div class="services">
  • Site Development<br>
  • Utility Construction • Excavation
</div>
<div class="address">
  40876 County Lane 19<br>
  Pell Harbor, FL 34000
</div>
</body>
</html>
```